Bluefern Capital Counsel Needs a Letterhead

Tomi, we need a letterhead/banner for our blog, which is titled "Quiet Harbor Chronicle". The letterhead/banner should incorporate the enclosed banner image, logo, and the name of our blog ("Quiet Harbor Chronicle").

We would also like an alternative design that includes our picture. Here, we have two options that we would like to see.

In all, we would like to see 3 different designs: one banner without any pics; and two banner with two versions of our pictures.

The file size should be able to be resized for the space given to us at our website (http://bluefern-capital-counsel.com).

We also need the letterhead/banner by Friday, June 13. Thanks!!

```html
<!DOCTYPE html>
<html lang="en">
<head>
<meta charset="utf-8">
<title>Quiet Harbor Chronicle — Bluefern Capital Counsel</title>
<link rel="stylesheet" href="https://fonts.googleapis.com/css2?family=Bebas+Neue&family=Roboto:wght@400&display=swap">
<style>
  :root {
    --ink: #000000;
    --headline: #f2ee8c;
    --rule: #5f5e36;
    --badge-bg: #2b2725;
    --badge-text: #e6e1d6;
    --photo-dark: #1a1a1a;
    --photo-mid: #6e6e6e;
    --photo-light: #b9b9b9;
  }
  * { margin: 0; padding: 0; box-sizing: border-box; }
  html, body {
    width: 1200px;
    height: 250px;
    overflow: hidden;
    background: var(--ink);
  }
  .banner {
    position: relative;
    width: 1200px;
    height: 250px;
    background: var(--ink);
    overflow: hidden;
  }
  .banner__photo {
    position: absolute;
    top: 0;
    left: 540px;
    width: 660px;
    height: 250px;
    background:
      radial-gradient(ellipse 160px 150px at 500px 110px, var(--photo-light), transparent 75%),
      radial-gradient(ellipse 130px 140px at 220px 100px, var(--photo-mid), transparent 75%),
      linear-gradient(90deg, var(--ink) 0%, var(--photo-dark) 25%, #3a3a3a 60%, #555 100%);
  }
  .banner__badge {
    position: absolute;
    left: 28px;
    top: 108px;
    width: 162px;
    height: 107px;
    background: var(--badge-bg);
    display: flex;
    flex-direction: column;
    align-items: center;
    justify-content: flex-end;
    padding-bottom: 14px;
    gap: 12px;
  }
  .banner__badge-mark {
    width: 26px;
    height: 26px;
    background: var(--badge-text);
    opacity: 0.8;
  }
  .banner__badge-name {
    font-family: "Roboto", Arial, sans-serif;
    font-weight: 400;
    font-size: 11.5px;
    color: var(--badge-text);
    text-align: center;
    line-height: 1.2;
  }
  .banner__title {
    position: absolute;
    left: 212px;
    top: 108px;
    font-family: "Bebas Neue", "Oswald", sans-serif;
    font-weight: 400;
    font-size: 100px;
    line-height: 1;
    letter-spacing: 0.5px;
    color: var(--headline);
    white-space: nowrap;
  }
  .banner__rule {
    position: absolute;
    left: 212px;
    top: 214px;
    width: 988px;
    height: 1px;
    background: var(--rule);
  }
</style>
</head>
<body>
  <header class="banner">
    <div class="banner__photo" role="img" aria-label="Black-and-white photograph of two smiling advisors in bow ties, fading into the black background"></div>
    <div class="banner__badge">
      <span class="banner__badge-mark"></span>
      <span class="banner__badge-name">Bluefern Capital Counsel</span>
    </div>
    <h1 class="banner__title">Quiet Harbor Chronicle</h1>
    <div class="banner__rule"></div>
  </header>
</body>
</html>
```